Tavrelo, Collaboration Ecosystem for the Integration of Logistics Services

We need a website to build Tavrelo logistics orchestration services, across America. The moonshot Tavrelo invites to integrate under a "logistics button" the entire supply chains of physical goods, to people, in cities (just as financial services do with their payment button in e-commerce) . Tavrelo is a commitment to the unimaginable, to obtain a stratospheric success, the company will be integrated with the academy and local governments, in the construction of: Common standards for the integration of services; Technologically validate the services; Develop product traceability technologies in exchanges between companies; Give regulatory and legal compliance in the automated delivery of products; and make payments within the supply chain with each delivery of products to a person.
The pandemic has challenged us as a species, it has shown us that human collaboration is essential to give our species sustainability. Today we cannot act alone and we need more collaboration mechanisms to satisfy our needs. Tavrelo is a journey into the unknown, an area of development outside the traditional models of logistics services in cities, everything has changed and will change again.
Tavrelo is a B2B business. Solves the delivery of products in an urban territory, integrates under a decentralized technological model of services to the different actors involved in the supply chains of each of the goods that people consume from their homes. For users, the Tavrelo delivery button implies the contracting of a service according to their requirements: The exact date and time of delivery, the value of caring for the environment, the technology involved in delivery, the importance of people and their well-being in the supply chain.
It is important that the design reflects technology, collaboration and sales explosion. We attach our logo.
Important points are: we are incorporating the companies through a membership to initially finance the project; we will have a launch event in November 2022; and we will carry out content and advertising campaigns to generate visibility for this initiative, which is revolutionary. Short-term objectives of the project are: to publicize the project through social networks and online to incorporate partner companies, publicize the November launch event and show the progress in the integration process of companies in the "logistics button Tavrelo. Finally, we would like the design to be adapted for the Wix platform.

Target Market(s)

Primary target: Big companies in the transportation and logistics services. Secondary target: Big companies in the rest of the economy.

Coding

Coded - Design and coding required

Number of Pages Required

5+ page

Font styles to use
Serif

Requirements
Must have
• Home to explain the project in one image
Spectacular Big Banner
Countdown with the project deadline: 365 days to launch the Tavrelo logistics button
Landing page for seminar inscriptions
Landing page for membership sales
Visually communicate high tech, collaboration and sales Big Bang for the companies that will participate
Once we have the initial group of companies, we need a a template to communicate the missions (as if we are going to the Moon or Mars) that the companies will commit. For instance, The Technology is a mission; International Funding is another mission; Integration is another mission, and so forth.
Nice to have
• Websites we love:

https://dune.kovrapi.org/

https://plemtarquavix.com/

https://www.dulverankosta.com/
Should not have
• Boring images, colors or whatever...

```html
<!DOCTYPE html>
<html lang="en">
<head>
<meta charset="utf-8">
<title>Tavrelo — Logistics Collaboration Ecosystem</title>
<link href="https://fonts.googleapis.com/css2?family=Roboto:wght@400;500;700&family=Rubik:wght@500;700&display=swap" rel="stylesheet">
<style>
:root{
  --blue:#5a72f4;
  --ink:#1d1d1f;
  --muted:#777;
  --hero-bg:#f5f4f0;
  --soft-bg:#f4f4f4;
  --footer:#333335;
  --topbar:#a6a6a6;
  --white:#fff;
}
*{box-sizing:border-box;margin:0;padding:0}
html,body{width:1200px;height:3673px;overflow:hidden}
body{position:relative;font-family:"Roboto",sans-serif;color:var(--ink);background:var(--white)}
.abs{position:absolute}
.center{left:0;width:1200px;text-align:center}
h2.section-title{position:absolute;left:0;width:1200px;text-align:center;font-family:"Rubik",sans-serif;font-weight:700;font-size:34px;letter-spacing:.3px}
.btn{position:absolute;display:flex;align-items:center;justify-content:center;gap:8px;background:var(--blue);color:var(--white);border-radius:30px;font-weight:500;font-size:16px;text-decoration:none}

.topbar{top:0;left:0;width:1200px;height:40px;background:var(--topbar);color:var(--white);font-size:13px;line-height:40px;text-align:center}
.nav{top:40px;left:0;width:1200px;height:85px;background:var(--white)}
.nav a{position:absolute;top:34px;font-size:15px;font-weight:500;color:var(--ink);text-decoration:none}
.nav .btn{top:24px;left:932px;width:155px;height:40px;font-size:15px;color:var(--white)}
.brand-bump{top:60px;left:503px;width:194px;height:122px;border-radius:0 0 97px 97px;background:var(--white);z-index:2;text-align:center}
.brand-mark{width:50px;height:50px;margin:4px auto 0;background:var(--blue);border-radius:8px}
.brand-name{margin-top:10px;font-family:"Rubik",sans-serif;font-weight:700;font-size:19px;letter-spacing:2px;color:#888}

.hero{top:125px;left:0;width:1200px;height:599px;background:var(--hero-bg)}
.hero h1{position:absolute;top:104px;left:0;width:1200px;text-align:center;font-family:"Rubik",sans-serif;font-weight:700;font-size:40px;letter-spacing:.5px}
.hero p{position:absolute;top:162px;left:300px;width:600px;text-align:center;font-size:17px;line-height:25px;color:#444}
.hero .btn{top:234px;left:467px;width:266px;height:50px;font-size:16px}
.hero-art{position:absolute;top:290px;left:50px;width:1100px;height:309px;background:linear-gradient(180deg,#eef0f6 0%,#dfe6f3 55%,#e9e3dc 100%);border-radius:60px 60px 0 0}

.band{top:724px;left:0;width:1200px;height:97px;background:var(--blue);color:var(--white);display:flex;align-items:center;justify-content:center;gap:26px;font-family:"Rubik",sans-serif;font-size:40px;font-weight:500;letter-spacing:1px}
.band b{font-weight:700}
.band .dot{width:52px;height:52px;border-radius:50%;border:4px solid var(--white)}

.benefit{position:absolute;top:994px;width:230px;text-align:center}
.benefit .icon{width:74px;height:74px;margin:0 auto;border-radius:50%;background:var(--white);box-shadow:0 3px 12px rgba(0,0,0,.12);display:flex;align-items:center;justify-content:center}
.benefit h3{margin-top:22px;font-size:16px;font-weight:500;line-height:23px}
.benefit p{margin-top:13px;font-size:14px;line-height:21px;color:var(--muted)}

.what-photo{top:1397px;left:0;width:600px;height:496px;background:linear-gradient(175deg,#e9a35a 0%,#7a6a70 30%,#3f5b7a 60%,#8a4a4a 100%)}
.what-panel{top:1397px;left:600px;width:600px;height:496px;background:var(--blue);color:var(--white)}
.what-panel h2{position:absolute;top:57px;left:48px;font-family:"Rubik",sans-serif;font-weight:700;font-size:30px;letter-spacing:.4px}
.what-panel ul{position:absolute;top:110px;left:48px;width:470px;list-style:none}
.what-panel li{position:relative;padding-left:29px;font-size:15px;line-height:24px;margin-bottom:11px}
.what-panel li svg{position:absolute;left:0;top:6px}
.what-panel .btn{top:409px;left:48px;width:199px;height:44px;background:var(--white);color:var(--blue);font-size:15px}

.reality{top:1893px;left:0;width:1200px;height:652px;background:var(--soft-bg)}
.reality-card{position:absolute;top:165px;width:473px;text-align:center}
.reality-card .photo{height:308px;box-shadow:0 2px 8px rgba(0,0,0,.12)}
.reality-card h3{margin-top:36px;font-size:18px;font-weight:500;letter-spacing:.2px}
.reality-card p{margin-top:14px;font-size:15px;line-height:23px;color:var(--muted)}

.member{position:absolute;top:2697px;width:250px;text-align:center}
.member .portrait{width:150px;height:150px;margin:0 auto;border-radius:50%;background:radial-gradient(circle at 50% 40%,#bdbdbd,#555)}
.member h4{margin-top:20px;font-size:17px;font-weight:700}
.member .role{margin-top:3px;font-size:11.5px;color:#888}
.member p{margin-top:12px;font-size:14px;line-height:19px;color:var(--muted)}

.client{position:absolute;top:3162px;width:166px;height:86px;background:var(--white);box-shadow:0 2px 10px rgba(0,0,0,.1);display:flex;align-items:center;justify-content:center;gap:8px;font-size:14px;font-weight:500;color:#444}
.client i{width:12px;height:12px;background:var(--blue);display:block}

.footer{top:3332px;left:0;width:1200px;height:341px;background:var(--footer);color:var(--white)}
.footer h5{position:absolute;top:46px;font-size:18px;font-weight:500}
.footer .links{position:absolute;top:96px;list-style:none;font-size:14px}
.footer .links li{height:27px}
.footer .news{position:absolute;top:86px;left:413px;width:372px;text-align:center;font-size:14px;line-height:25px}
.footer .email{position:absolute;top:161px;left:413px;width:372px;height:41px;border:1px solid var(--white);border-radius:22px;display:flex;align-items:center;padding-left:20px;font-size:14px}
.footer .email span.arrow{position:absolute;right:0;top:-1px;width:50px;height:41px;background:var(--white);border-radius:0 22px 22px 0;display:flex;align-items:center;justify-content:center}
.footer .social{position:absolute;top:240px;left:0;width:1200px;display:flex;justify-content:center;gap:18px}
.footer .social i{width:13px;height:13px;border-radius:50%;background:var(--white);display:block}
.footer .contact{position:absolute;top:96px;left:917px;font-size:14px;line-height:20px}
.footer hr{position:absolute;top:281px;left:110px;width:980px;border:0;border-top:1px solid #555}
.footer .copy{position:absolute;top:298px;left:0;width:1200px;text-align:center;font-size:14px}
</style>
</head>
<body>

<div class="abs topbar">Lorem ipsum dolor sit amet, consectetur</div>

<nav class="abs nav">
  <a style="left:111px">Home</a>
  <a style="left:184px">About Us</a>
  <a style="left:278px">Our Services</a>
  <a style="left:395px">Benefits</a>
  <a style="left:721px">Value</a>
  <a style="left:789px">Blog</a>
  <a style="left:851px">Contact</a>
  <a class="btn">Logistics Button</a>
</nav>
<div class="abs brand-bump">
  <div class="brand-mark"></div>
  <div class="brand-name">TAVRELO</div>
</div>

<section class="abs hero">
  <h1>TAVRELO MOONSHOT</h1>
  <p>Lorem ipsum dolor sit amet, consectetur adipiscing elit, sed do eiusmod tempor incididunt ut labore amet, consectetur.</p>
  <a class="btn">SEMINAR INSCRIPTIONS
    <svg width="16" height="16" viewBox="0 0 16 16"><circle cx="8" cy="8" r="8" fill="#fff"/><path d="M6.5 4.5 10 8l-3.5 3.5" stroke="#5a72f4" stroke-width="2" fill="none"/></svg></a>
  <div class="hero-art" role="img" aria-label="Illustration of a city street with delivery drones carrying parcels, shoppers, a central online store screen and a delivery truck"></div>
</section>

<div class="abs band"><span class="dot"></span><span>OPERATING IN <b>365</b> DAYS</span></div>

<h2 class="section-title" style="top:896px">OUR BENEFITS</h2>

<div class="benefit" style="left:93px">
  <div class="icon"><svg width="38" height="38" viewBox="0 0 38 38" fill="none" stroke="#5a72f4" stroke-width="1.6"><path d="M4 15 19 5l15 10v19H4z"/><rect x="11" y="20" width="16" height="14"/><path d="M11 25h16M11 30h16"/></svg></div>
  <h3>Use your full capacity<br>and more</h3>
  <p>Lorem ipsum dolor sit amet, consie etur adipiscing elit.</p>
</div>
<div class="benefit" style="left:354px">
  <div class="icon"><svg width="38" height="38" viewBox="0 0 38 38" fill="none" stroke="#5a72f4" stroke-width="1.6"><rect x="6" y="4" width="26" height="30"/><path d="M6 14h26M6 24h26"/><rect x="11" y="7" width="7" height="5"/><rect x="20" y="17" width="7" height="5"/><rect x="11" y="27" width="7" height="5"/></svg></div>
  <h3>More efficient inventories<br>and stocks</h3>
  <p>Lorem ipsum dolor sit amet, consie etur adipiscing elit.</p>
</div>
<div class="benefit" style="left:616px">
  <div class="icon"><svg width="40" height="38" viewBox="0 0 40 38" fill="none" stroke="#5a72f4" stroke-width="1.6"><rect x="3" y="10" width="22" height="16"/><path d="M25 15h7l5 6v5H25z"/><circle cx="10" cy="28" r="3"/><circle cx="31" cy="28" r="3"/></svg></div>
  <h3>Greater use of transport<br>capacity</h3>
  <p>Lorem ipsum dolor sit amet, consie etur adipiscing elit.</p>
</div>
<div class="benefit" style="left:877px">
  <div class="icon"><svg width="38" height="38" viewBox="0 0 38 38" fill="none" stroke="#5a72f4" stroke-width="1.6"><rect x="4" y="12" width="30" height="18" rx="2"/><circle cx="19" cy="21" r="4"/><path d="M8 12l18-6 3 6"/></svg></div>
  <h3>Coordinate and efficient<br>payment system</h3>
  <p>Lorem ipsum dolor sit amet, consie etur adipiscing elit.</p>
</div>

<a class="btn" style="top:1244px;left:506px;width:188px;height:49px;font-size:15px">SEE ALL BENEFITS</a>

<div class="abs what-photo" role="img" aria-label="Aerial photo of a container port with cranes and a city skyline at sunset"></div>
<section class="abs what-panel">
  <h2>WHAT IS TAVRELO</h2>
  <ul>
    <li><svg width="14" height="14" viewBox="0 0 14 14"><circle cx="7" cy="7" r="7" fill="#fff"/><path d="M3.8 7.2 6 9.3l4.2-4.4" stroke="#5a72f4" stroke-width="1.8" fill="none"/></svg>Access ondemand to sell logistics services</li>
    <li><svg width="14" height="14" viewBox="0 0 14 14"><circle cx="7" cy="7" r="7" fill="#fff"/><path d="M3.8 7.2 6 9.3l4.2-4.4" stroke="#5a72f4" stroke-width="1.8" fill="none"/></svg>Access to logistics services to consume</li>
    <li><svg width="14" height="14" viewBox="0 0 14 14"><circle cx="7" cy="7" r="7" fill="#fff"/><path d="M3.8 7.2 6 9.3l4.2-4.4" stroke="#5a72f4" stroke-width="1.8" fill="none"/></svg>Collaboration ecosystem in a given territorial environment</li>
    <li><svg width="14" height="14" viewBox="0 0 14 14"><circle cx="7" cy="7" r="7" fill="#fff"/><path d="M3.8 7.2 6 9.3l4.2-4.4" stroke="#5a72f4" stroke-width="1.8" fill="none"/></svg>Solves integral problemof spot logistics, by connecting alloperators in a network</li>
    <li><svg width="14" height="14" viewBox="0 0 14 14"><circle cx="7" cy="7" r="7" fill="#fff"/><path d="M3.8 7.2 6 9.3l4.2-4.4" stroke="#5a72f4" stroke-width="1.8" fill="none"/></svg>Allowsbusinessmodelswith 100% flexible logistics services</li>
    <li><svg width="14" height="14" viewBox="0 0 14 14"><circle cx="7" cy="7" r="7" fill="#fff"/><path d="M3.8 7.2 6 9.3l4.2-4.4" stroke="#5a72f4" stroke-width="1.8" fill="none"/></svg>Logisticsoptimization in theurban ecosystem</li>
    <li><svg width="14" height="14" viewBox="0 0 14 14"><circle cx="7" cy="7" r="7" fill="#fff"/><path d="M3.8 7.2 6 9.3l4.2-4.4" stroke="#5a72f4" stroke-width="1.8" fill="none"/></svg>Document, payment and human resources management</li>
  </ul>
  <a class="btn">MEMBERSHIP SALES</a>
</section>

<section class="abs reality">
  <h2 class="section-title" style="top:82px">REALITY &amp; FUTURE</h2>
  <div class="reality-card" style="left:111px">
    <div class="photo" role="img" aria-label="Photo of a single bee in flight over a soft green and yellow background" style="background:radial-gradient(circle at 62% 62%,#f1d64a 0%,#8bbf4a 25%,#3f9a5a 60%,#2f7a4a 100%)"></div>
    <h3>A WORLD WITHOUT COLLABORATION</h3>
    <p>Lorem ipsum dolor sit amet, consectetur adipiscing elit, sed do eiusmod tempor incididunt ut labore.</p>
  </div>
  <div class="reality-card" style="left:616px">
    <div class="photo" role="img" aria-label="Photo of many bees working together on a honeycomb" style="background:linear-gradient(135deg,#c98a3a,#7a4f22 50%,#d9a45a)"></div>
    <h3>A WORLD WITH COLLABORATION</h3>
    <p>Lorem ipsum dolor sit amet, consectetur adipiscing elit, sed do eiusmod tempor incididunt ut labore.</p>
  </div>
</section>

<h2 class="section-title" style="top:2610px">OUR TEAM</h2>

<div class="member" style="left:80px">
  <div class="portrait" role="img" aria-label="Black and white portrait of Darío Venquel"></div>
  <h4>Darío Venquel</h4><div class="role">CEO - Tavrelo</div>
  <p>Technological &nbsp; entrepreneur<br>:Founder Norvik Advisors</p>
</div>
<div class="member" style="left:342px">
  <div class="portrait" role="img" aria-label="Black and white portrait of Tomás Arbeló"></div>
  <h4>Tomás Arbeló</h4><div class="role">Partner director</div>
  <p>Director of the Center of Transport<br>and Logistics UNVL</p>
</div>
<div class="member" style="left:606px">
  <div class="portrait" role="img" aria-label="Black and white portrait of Iván Corlesa"></div>
  <h4>Iván Corlesa</h4><div class="role">Partner director</div>
  <p>Academic Director Center Transport<br>and Logistics UNVL</p>
</div>
<div class="member" style="left:868px">
  <div class="portrait" role="img" aria-label="Black and white portrait of Rafael Dunstano"></div>
  <h4>Rafael Dunstano</h4><div class="role">Director of Marketing</div>
  <p>Expert advisor in marketing,B2B<br>sales and communications</p>
</div>

<h2 class="section-title" style="top:3074px">OUR CLIENTS</h2>
<div class="client" style="left:118px"><i></i>Univ. Norvela</div>
<div class="client" style="left:316px"><i></i>Centro Travesa</div>
<div class="client" style="left:515px"><i></i>Kestrel Scale</div>
<div class="client" style="left:714px"><i></i>Cámara Orvanta</div>
<div class="client" style="left:913px"><i></i>Quenlix</div>

<footer class="abs footer">
  <h5 style="left:110px">Quick Links</h5>
  <ul class="links" style="left:110px"><li>Home</li><li>About Us</li><li>Our Services</li><li>Benefits</li><li>Value</li><li>Contact</li></ul>
  <ul class="links" style="left:226px"><li>Terms &amp; Condition</li><li>Privacy Policy</li><li>Support</li><li>Imprint</li><li>Contact</li></ul>
  <h5 style="left:0;width:1200px;text-align:center">Inbox Goodies</h5>
  <p class="news">Sign up to receive updates, subscription offers<br>and alerts on limited-edition boxes</p>
  <div class="email">Email*<span class="arrow"><svg width="18" height="10" viewBox="0 0 18 10"><path d="M0 5h16M12 1l4 4-4 4" stroke="#333" stroke-width="2" fill="none"/></svg></span></div>
  <div class="social"><i></i><i></i><i></i><i></i></div>
  <h5 style="left:917px">Contact Us</h5>
  <div class="contact">218 Calder Lane<br>Westbrook, CA 94012<br><br>info@tavrelo.com<br><br>555-019-2841</div>
  <hr>
  <div class="copy">Copyrights 2021 TAVRELO. All Rights Reserved</div>
</footer>

</body>
</html>
```